Healthy Lifestyle Vitamin Supplement Company needs a web site designed.

We are starting a new website for selling quality natural vitamins and supplements online plus providing news and information on healthy living. We DO NOT need any programming done for this site. Just the design in a layered photoshop file. This site needs to communicate that we are the authoritative source for healthy living and a trusted place to buy supplements and information on living a healthy lifestyle.

Triggers On page will be

Trigger set 1
Home - Shop By Brand - Top Sellers - Clearance - Help Center - My Favorites

Trigger set 2
Vitamins and Herbs - Natural Living - Aromatherapy - Coffee and Tea - Health and Beauty - Healthy Foods - Pet Health - Sports and Diet

Triggers Other
Login - Shopping Cart - Checkout - Track Order

Need a search bar in the design

Left side should be categories look at Verolane.com for example of categories.

Name and domain name is Brisk Meadow Crest

Will also need a logo to go along with that.

```html
<!DOCTYPE html>
<html lang="en">
<head>
<meta charset="utf-8">
<title>Brisk Meadow Crest — Vitamins &amp; Supplements</title>
<link rel="stylesheet" href="https://fonts.googleapis.com/css2?family=Arimo:wght@400;700&family=Roboto+Slab:wght@600&family=Cabin:ital@1&display=swap">
<style>
  :root {
    --berry: #a8325e;
    --berry-dark: #8e2550;
    --berry-light: #c24a78;
    --rose: #c9679a;
    --rose-band: #d87a98;
    --blush: #f3d7e2;
    --white: #ffffff;
    --ink: #222222;
    --wine: #7a1030;
    --price: #e0121b;
    --card-line: #8f8fd6;
    --tab-grey: #dedede;
    --footer-link: #ecd3dd;
    --arrow: #9fc9da;
  }
  * { box-sizing: border-box; margin: 0; padding: 0; }
  html, body { width: 1200px; height: 1000px; overflow: hidden; }
  body {
    position: relative;
    font-family: "Arimo", Arial, sans-serif;
    background: linear-gradient(160deg, #f7f7f7 0%, #e4e4e4 40%, #f4f4f4 70%, #e2e2e2 100%);
    color: var(--ink);
  }
  .abs { position: absolute; }

  /* Header */
  .site-header {
    left: 5px; top: 5px; width: 1190px; height: 108px;
    background: linear-gradient(180deg, var(--berry-light) 0%, var(--berry) 55%, var(--berry-dark) 100%);
  }
  .brand-name {
    left: 36px; top: 14px;
    font-family: "Arimo", sans-serif; font-weight: 700; font-size: 40px;
    color: #f7c9dc; letter-spacing: 0.5px;
  }
  .utility-links { left: 737px; top: 8px; font-size: 16px; color: var(--white); display: flex; }
  .utility-links span { white-space: pre; }
  .hotline { left: 738px; top: 33px; display: flex; align-items: center; gap: 8px; color: var(--white); font-weight: 700; font-size: 17px; }
  .search { left: 920px; top: 33px; width: 238px; height: 23px; display: flex; }
  .search-field { width: 197px; height: 22px; border-radius: 11px 0 0 11px; background: linear-gradient(180deg, #ffffff, #d9d9d9); }
  .search-go { width: 41px; height: 23px; border-radius: 0 6px 6px 0; background: #6e1538; color: var(--white); font-size: 12px; font-weight: 700; display: flex; align-items: center; justify-content: center; }
  .main-nav { left: 5px; top: 68px; width: 1190px; height: 45px; border-top: 1px solid #c0527d; }
  .main-nav a {
    position: absolute; top: 0; height: 45px; line-height: 40px;
    color: var(--white); text-decoration: none; font-size: 15px; font-weight: 700;
  }
  .main-nav .divider { position: absolute; top: 0; width: 1px; height: 45px; background: #c95d87; }
  .main-nav .current::after { content: ""; position: absolute; left: -6px; right: -6px; bottom: 2px; height: 3px; background: #e8a4c0; }

  /* Category tabs */
  .tab {
    top: 120px; height: 41px; border-radius: 8px 8px 3px 3px;
    background: linear-gradient(180deg, #f5f5f5, var(--tab-grey));
    font-size: 15px; color: #222; display: flex; align-items: center; justify-content: center;
    box-shadow: 0 1px 2px rgba(0,0,0,.2);
  }
  .tab.active { background: linear-gradient(180deg, #f3c6da, #d36c9c); }

  /* Sidebar */
  .category-panel { left: 37px; top: 174px; width: 266px; border: 1px solid #b7b7c9; background: var(--white); z-index: 2; }
  .category-title { height: 83px; display: flex; align-items: center; justify-content: center; font-size: 30px; font-weight: 700; color: #444; letter-spacing: 1px; }
  .category-list { list-style: none; }
  .category-list li {
    background: var(--rose); color: var(--white);
    font-family: "Roboto Slab", Georgia, serif; font-weight: 600; font-size: 16px;
    display: flex; align-items: center; justify-content: center;
    border-top: 2px solid #b4b4dc;
  }

  /* Hero */
  .hero-art { left: 309px; top: 175px; width: 599px; height: 198px; background: radial-gradient(circle at 68% 55%, #f6dbe6 0%, #d79bb5 45%, #b87797 100%); }
  .hero-products { left: 330px; top: 180px; width: 300px; height: 190px; border-radius: 20px; background: linear-gradient(180deg, #f1ecd9, #ffc04a 50%, #e8e2cc); opacity: .85; }
  .hero-caption { left: 640px; top: 230px; width: 260px; text-align: center; font-family: "Roboto Slab", Georgia, serif; font-weight: 600; font-size: 27px; line-height: 34px; color: #8a1d3e; }
  .promo-list { left: 911px; top: 175px; width: 252px; }
  .promo-list li {
    list-style: none; height: 37px; margin-bottom: 3px; padding-left: 24px;
    background: linear-gradient(90deg, var(--blush), #f8e9ef);
    font-family: "Cabin", sans-serif; font-style: italic; font-size: 19px; color: #111;
    display: flex; align-items: center;
  }
  .shipping-band { left: 5px; top: 374px; width: 1190px; height: 73px; background: var(--rose-band); z-index: 1; }
  .shipping-band p { position: absolute; left: 494px; top: 22px; font-size: 30px; color: var(--white); letter-spacing: .5px; }

  /* Products */
  .product-bar { left: 303px; top: 455px; width: 862px; height: 26px; background: #e2e2e2; }
  .product-label { top: 459px; width: 212px; text-align: center; font-size: 17px; color: #222; }
  .product-card { top: 482px; width: 213px; height: 316px; border: 1px solid var(--card-line); border-radius: 9px; background: #f4f4f4; }
  .product-photo { position: absolute; left: 12px; top: 5px; width: 186px; height: 176px; border-radius: 50%; border: 2px solid #e5e2d5; background: radial-gradient(circle, #ffffff 30%, #f0f0f0 100%); }
  .product-photo i { position: absolute; left: 50%; top: 10px; width: 84px; height: 154px; margin-left: -42px; border-radius: 14px 14px 8px 8px; }
  .product-type { position: absolute; top: 196px; width: 100%; text-align: center; font-size: 17px; color: var(--wine); }
  .product-desc { position: absolute; left: 6px; top: 227px; width: 202px; font-size: 11px; line-height: 13px; color: #000; }
  .product-price { position: absolute; left: 7px; top: 271px; font-size: 16px; color: var(--price); }
  .add-to-cart { position: absolute; left: 79px; top: 267px; width: 127px; height: 25px; border-radius: 5px; background: linear-gradient(180deg, #cf3d70, #9b1f4a); color: var(--white); font-size: 14px; display: flex; align-items: center; justify-content: center; }

  /* Carousel */
  .carousel-text { top: 804px; font-size: 14px; line-height: 16px; color: #111; }
  .thumb { top: 802px; width: 16px; height: 32px; border-radius: 4px; }

  /* Footer */
  .site-footer { left: 5px; top: 843px; width: 1190px; height: 152px; background: var(--berry); }
  .footer-col { top: 854px; }
  .footer-col h3 { font-weight: 400; font-size: 29px; color: var(--white); margin-bottom: 18px; }
  .footer-col ul { list-style: none; padding-left: 3px; }
  .footer-col li { font-size: 17px; line-height: 21.5px; color: var(--footer-link); }
  .newsletter-field { left: 875px; top: 906px; width: 220px; height: 30px; border-radius: 15px; background: var(--white); box-shadow: inset 0 0 4px rgba(0,0,0,.3); }
  .subscribe { left: 979px; top: 953px; width: 116px; height: 23px; border-radius: 12px; background: #d889ad; font-size: 14px; color: #111; display: flex; align-items: center; justify-content: center; }
</style>
</head>
<body>

<header>
  <div class="abs site-header"></div>
  <div class="abs brand-name">Brisk Meadow Crest</div>
  <nav class="abs utility-links">
    <span>Shopping Cart     |    Checkout    |    Track Order     |    Log In</span>
  </nav>
  <div class="abs hotline">
    <svg width="18" height="28" viewBox="0 0 18 28" aria-hidden="true"><path d="M4 2 L9 2 L10 8 L7 10 Q8 16 11 19 L14 17 L17 22 L14 26 Q3 22 2 6 Z" fill="#2b2b2b" stroke="#888" stroke-width="1"/></svg>
    <span>18004271</span>
  </div>
  <div class="abs search"><div class="search-field"></div><div class="search-go">GO</div></div>
  <nav class="abs main-nav">
    <a class="current" style="left:68px">Home</a>
    <span class="divider" style="left:123px"></span>
    <a style="left:141px">Shop By Brand</a>
    <span class="divider" style="left:257px"></span>
    <a style="left:274px">Top Sellers</a>
    <span class="divider" style="left:367px"></span>
    <a style="left:383px">Clearance</a>
    <span class="divider" style="left:466px"></span>
    <a style="left:480px">Help Center</a>
    <span class="divider" style="left:574px"></span>
    <a style="left:589px">My Favorites</a>
  </nav>
</header>

<nav>
  <div class="abs tab active" style="left:37px;width:158px">Vitamins and Herbs</div>
  <div class="abs tab" style="left:200px;width:129px">Natural Living</div>
  <div class="abs tab" style="left:335px;width:123px">Aromatherapy</div>
  <div class="abs tab" style="left:463px;width:143px">Coffee and Tea</div>
  <div class="abs tab" style="left:611px;width:153px">Health and Beauty</div>
  <div class="abs tab" style="left:769px;width:132px">Healthy Foods</div>
  <div class="abs tab" style="left:907px;width:98px">Pet Health</div>
  <div class="abs tab" style="left:1011px;width:151px">Sports and Diet</div>
</nav>

<aside class="abs category-panel">
  <div class="category-title">CATEGORY</div>
  <ul class="category-list">
    <li style="height:39px">A &amp; D Vitamins</li>
    <li style="height:39px">Acidophilus/Probiotics</li>
    <li style="height:36px">Amino Acid Supplements</li>
    <li style="height:40px">Antioxidants</li>
    <li style="height:40px">A &amp; D Vitamins</li>
    <li style="height:38px">Acidophilus/Probiotics</li>
    <li style="height:37px">Amino Acid Supplements</li>
    <li style="height:46px">Acidophilus/Probiotics</li>
    <li style="height:39px">Acidophilus/Probiotics</li>
    <li style="height:41px">Antioxidants</li>
  </ul>
</aside>

<section>
  <div class="abs hero-art" role="img" aria-label="Soft pink swirl backdrop for the featured supplement range"></div>
  <div class="abs hero-products" role="img" aria-label="Group of supplement bottles from the featured range"></div>
  <div class="abs hero-caption">Brisk Meadow Crest<br>Products</div>
  <ul class="abs promo-list">
    <li>Shop Our Vast Collections</li>
    <li>Holi Day Shop</li>
    <li>Beauty Products</li>
    <li>Festives Gifts</li>
    <li>Day Sale</li>
  </ul>
  <div class="abs shipping-band"><p>FREE SHIPPING</p></div>
</section>

<section>
  <div class="abs product-bar"></div>
  <div class="abs product-label" style="left:375px">Product Name</div>
  <div class="abs product-label" style="left:626px">Product Name</div>
  <div class="abs product-label" style="left:867px">Product Name</div>

  <article class="abs product-card" style="left:386px">
    <div class="product-photo" role="img" aria-label="Nutritional shake mix canister"><i style="background:linear-gradient(180deg,#f2f2f2 0%,#f2f2f2 30%,#f39a3d 40%,#f6c77a 75%,#eaeaea 100%)"></i></div>
    <div class="product-type">Type of Name</div>
    <p class="product-desc">Lorem Ipsum is simply dummy text of the printing and typesetting industry.</p>
    <div class="product-price">$120</div>
    <div class="add-to-cart">ADD TO CART</div>
  </article>

  <article class="abs product-card" style="left:627px">
    <div class="product-photo" role="img" aria-label="Calcium supplement bottle"><i style="background:linear-gradient(180deg,#fafafa 0%,#dcdcdc 35%,#c8ccd2 60%,#eeeeee 100%)"></i></div>
    <div class="product-type">Type of Name</div>
    <p class="product-desc">Lorem Ipsum is simply dummy text of the printing and typesetting industry.</p>
    <div class="product-price">$130</div>
    <div class="add-to-cart">ADD TO CART</div>
  </article>

  <article class="abs product-card" style="left:870px">
    <div class="product-photo" role="img" aria-label="Sports vitamin and mineral supplement bottle"><i style="background:linear-gradient(180deg,#e8e8e8 0%,#c9c9c9 20%,#a8c64a 35%,#9bbb3c 70%,#222 100%)"></i></div>
    <div class="product-type">Type of Name</div>
    <p class="product-desc">Lorem Ipsum is simply dummy text of the printing and typesetting industry.</p>
    <div class="product-price">$120</div>
    <div class="add-to-cart">ADD TO CART</div>
  </article>
</section>

<section>
  <svg class="abs" style="left:36px;top:804px" width="26" height="28" viewBox="0 0 26 28" aria-label="Previous"><path d="M2 2 L24 14 L2 26 Z" fill="var(--arrow)" stroke="#6c9fb4"/></svg>
  <span class="abs thumb" style="left:105px;background:linear-gradient(180deg,#eee,#f39a3d)" role="img" aria-label="Shake mix thumbnail"></span>
  <p class="abs carousel-text" style="left:153px">Lorem Ipsum is simply<br>dummy text of the printing</p>
  <span class="abs thumb" style="left:372px;background:linear-gradient(180deg,#555,#6b2a2a)" role="img" aria-label="Dark supplement bottle thumbnail"></span>
  <p class="abs carousel-text" style="left:420px">Lorem Ipsum is simply<br>dummy text of the printing</p>
  <span class="abs thumb" style="left:636px;width:20px;background:linear-gradient(180deg,#ccc,#9bbb3c,#222)" role="img" aria-label="Green supplement bottle thumbnail"></span>
  <p class="abs carousel-text" style="left:689px">Lorem Ipsum is simply<br>dummy text of the printing</p>
  <span class="abs thumb" style="left:876px;background:linear-gradient(180deg,#555,#6b2a2a)" role="img" aria-label="Dark supplement bottle thumbnail"></span>
  <p class="abs carousel-text" style="left:938px">Lorem Ipsum is simply<br>dummy text of the printing</p>
  <svg class="abs" style="left:1135px;top:804px" width="26" height="28" viewBox="0 0 26 28" aria-label="Next"><path d="M24 2 L2 14 L24 26 Z" fill="var(--arrow)" stroke="#6c9fb4"/></svg>
</section>

<footer>
  <div class="abs site-footer"></div>
  <div class="abs footer-col" style="left:37px">
    <h3>Company</h3>
    <ul><li>About Us</li><li>Contact Us</li><li>Customer Servic</li><li>Privacy Policy</li></ul>
  </div>
  <div class="abs footer-col" style="left:300px">
    <h3>Quicks Links</h3>
    <ul><li>Site Map</li><li>Search Terms</li><li>Advanced Search</li></ul>
  </div>
  <div class="abs footer-col" style="left:602px">
    <h3>My Account</h3>
    <ul><li>My Cart</li><li>My Wishlist</li><li>Check Out</li></ul>
  </div>
  <div class="abs footer-col" style="left:869px">
    <h3>News Letter</h3>
  </div>
  <div class="abs newsletter-field"></div>
  <div class="abs subscribe">Subscribe</div>
</footer>

</body>
</html>
```